To design a look and feel for a website. The company offers technical services to governemtns and public bodies. It does NOT market to the public.

The core business is GIS (Geographic Information Systems)

The site needs to be clean and simple, The current version is available here: www.velda.ie

Target Market(s)

Goverment agencies and public bodies in the EU, buying through the public procurerment process

Requirements
Should not have
• corny graphics of hands holding globes or sateliites please.

```html
<!DOCTYPE html>
<html lang="en">
<head>
<meta charset="utf-8">
<title>VELDA Group – Information Expertise</title>
<link rel="stylesheet" href="https://fonts.googleapis.com/css2?family=Source+Sans+3:wght@400;600;700&family=Maven+Pro:wght@400;500&display=swap">
<style>
:root{
  --page-bg:#ececec;
  --panel:#ffffff;
  --navy:#1a2a4a;
  --brand-blue:#2a78b8;
  --rule-blue:#2c79b6;
  --text:#4a4a4a;
  --text-soft:#6a6a6a;
  --heading:#555c63;
  --card-border:#dcdcdc;
  --logo-navy:#24346b;
}
*{box-sizing:border-box;margin:0;padding:0}
html,body{width:1200px;height:1055px;overflow:hidden}
body{background:var(--page-bg);font-family:"Source Sans 3",Arial,sans-serif;color:var(--text);position:relative}
a{color:inherit;text-decoration:none}

.site-logo{position:absolute;left:64px;top:50px;display:flex;align-items:center;gap:8px;color:var(--logo-navy);font-family:"Maven Pro",sans-serif;font-size:26px;font-weight:500;line-height:1}
.site-logo .dot{width:12px;height:12px;border-radius:50%;background:var(--logo-navy)}

.main-nav{position:absolute;left:476px;top:51px;display:flex}
.main-nav a{font-family:"Maven Pro",sans-serif;font-size:18px;color:#6d6d6d;height:34px;line-height:34px;padding:0 16px;margin-right:18px}
.main-nav a.is-active{background:var(--navy);color:#fff;border-bottom:2px solid #6c7fa8}
.join-button{position:absolute;left:1049px;top:49px;width:87px;height:33px;background:linear-gradient(#3b8fd0,#1f6aad);color:#fff;font-family:"Maven Pro",sans-serif;font-size:18px;text-align:center;line-height:32px}

.content-panel{position:absolute;left:62px;top:111px;width:1074px;height:870px;background:var(--panel);box-shadow:0 1px 4px rgba(0,0,0,.15)}

.social-links{position:absolute;right:20px;top:12px;display:flex;gap:8px;font-size:11px;color:var(--text-soft)}
.social-links a{display:flex;align-items:center;gap:3px}
.social-links i{width:12px;height:12px;background:#8a9aa9;display:inline-block}

.hero{position:absolute;left:50px;top:44px;width:977px;height:270px;background:linear-gradient(100deg,#1f4fd6 0%,#2a7ef0 35%,#39c6f2 60%,#1b61e0 100%)}
.hero-caption{position:absolute;left:0;top:93px;width:510px;height:138px;background:rgba(30,50,110,.85);color:#fff;font-family:"Maven Pro",sans-serif;padding:12px 18px 0}
.hero-caption p{font-size:32px;line-height:39px;font-weight:500}
.hero-caption .light{font-weight:400;font-size:27px}

.info-card{position:absolute;top:342px;height:308px;border:1px solid var(--card-border);background:#fff;padding:12px 12px 0}
.info-card h2{font-family:"Maven Pro",sans-serif;font-weight:400;font-size:23px;color:var(--heading);padding-bottom:4px;border-bottom:2px solid var(--rule-blue)}
.info-card p{font-size:12.4px;line-height:17.6px;margin-top:14px}
.about{left:50px;width:306px}
.services{left:385px;width:297px}
.news{left:720px;width:306px}
.service-list{list-style:none;margin-top:12px}
.service-list li{font-size:12.4px;line-height:23.4px;padding-left:12px;position:relative;white-space:nowrap}
.service-list li::before{content:"";position:absolute;left:1px;top:9px;border-left:4px solid #666;border-top:3px solid transparent;border-bottom:3px solid transparent}
.news .lead{font-weight:700;color:#555;margin-top:20px;line-height:16px}
.news .body{text-align:justify;line-height:15.4px}
.more-button{position:absolute;right:12px;bottom:13px;width:74px;height:23px;background:linear-gradient(#3b8fd0,#1f6aad);color:#fff;font-family:"Maven Pro",sans-serif;font-size:16px;text-align:center;line-height:22px}

.clients{position:absolute;left:48px;top:691px;width:979px;height:150px;background:#f2f2f2;padding:0 25px 0 30px}
.clients-head{display:flex;justify-content:space-between;align-items:flex-end;height:42px;border-bottom:2px solid var(--rule-blue)}
.clients-head h2{font-family:"Maven Pro",sans-serif;font-weight:400;font-size:25px;color:var(--heading);line-height:1;padding-bottom:4px}
.see-all{font-family:"Maven Pro",sans-serif;font-size:15px;color:#444;display:flex;align-items:center;gap:12px;padding-bottom:10px}
.client-strip{margin-top:22px;height:65px;background:#fff;box-shadow:0 2px 3px rgba(0,0,0,.2);display:flex;align-items:center;justify-content:space-around;padding:0 10px}
.client-name{font-size:18px;font-weight:700;color:#555}
.client-badge{width:40px;height:34px;border-radius:50%;background:#777}
.client-badge.square{border-radius:3px;width:70px;height:26px;background:#9a9a9a}

.carousel-arrow{position:absolute;top:865px}
.carousel-arrow.prev{left:22px}
.carousel-arrow.next{left:1152px}

.site-footer{position:absolute;left:122px;top:1008px;width:968px;display:flex;justify-content:space-between;font-size:12px;color:#333}
.footer-nav a{font-family:"Maven Pro",sans-serif;letter-spacing:.5px}
.footer-nav span{margin:0 6px;color:#777}
</style>
</head>
<body>

<a class="site-logo" href="#"><span class="dot"></span>VELDA Group</a>

<nav class="main-nav">
  <a class="is-active" href="#">Home</a>
  <a href="#">Services</a>
  <a href="#">Clients</a>
  <a href="#">Contact</a>
  <a href="#">Inspire</a>
</nav>
<a class="join-button" href="#">Join</a>

<main class="content-panel">
  <div class="social-links">
    <a href="#"><i></i>Orbit</a>
    <a href="#"><i></i>Kinfolk</a>
    <a href="#"><i></i>Chirp</a>
  </div>

  <section class="hero" role="img" aria-label="Blue world map with keypad and grid lines">
    <div class="hero-caption">
      <p><span class="light">VELDA’s</span> Quality Management System <span class="light">is</span> ISO 9001:2008 <span class="light">certified</span></p>
    </div>
  </section>

  <article class="info-card about">
    <h2>About Us</h2>
    <p>The VELDA Group has been in business since 1994 and continues to develop and update its range of services. The company has a high level of expertise in handling data and information, and in building and re-engineering database systems. We have a particular expertise in working with Irish data sets and have a strong grounding in dealing with spatial data.</p>
    <p>The company’s Quality Management System is ISO 9001:2008 certified (reviewed Jan 2012)</p>
    <a class="more-button" href="#">More</a>
  </article>

  <article class="info-card services">
    <h2>Services</h2>
    <ul class="service-list">
      <li>Lorem ipsum dolor sit amet, consectetur adipisicing</li>
      <li>Lorem ipsum dolor sit amet, consectetur adipisicing</li>
      <li>Lorem ipsum dolor sit amet, consectetur adipisicing</li>
      <li>Lorem ipsum dolor sit amet, consectetur adipisicing</li>
      <li>Lorem ipsum dolor sit amet, consectetur adipisicing</li>
      <li>Lorem ipsum dolor sit amet, consectetur adipisicing</li>
      <li>Lorem ipsum dolor sit amet, consectetur adipisicing</li>
      <li>Lorem ipsum dolor sit amet, consectetur adipisicing</li>
    </ul>
    <a class="more-button" href="#">More</a>
  </article>

  <article class="info-card news">
    <h2>Latest News</h2>
    <p class="lead">Lorem ipsum dolor sit amet, consectetur adipisicing elit, sed do eiusmod tempor</p>
    <p class="body">Lorem ipsum dolor sit amet, consectetur adipisicing elit, sed do eiusmod tempor incididunt ut labore et dolore magna aliqua. Ut enim ad minim veniam, quis nostrud exercitation ullamco laboris nisi ut aliquip ex ea commodo Lorem ipsum dolor sit amet, consectetur adipisicing elit, sed do eiusmod tempor incididunt ut labore et dolore magna aliqua.</p>
    <a class="more-button" href="#">More</a>
  </article>

  <section class="clients">
    <div class="clients-head">
      <h2>Our Clients</h2>
      <a class="see-all" href="#">See All
        <svg width="8" height="12" viewBox="0 0 8 12"><path d="M0 0L8 6L0 12Z" fill="#444"/></svg>
      </a>
    </div>
    <div class="client-strip">
      <span class="client-name">Halden</span>
      <span class="client-badge" aria-label="Security badge"></span>
      <span class="client-badge square" aria-label="Privacy certificate"></span>
      <span class="client-badge" aria-label="Trust seal"></span>
      <span class="client-name">Corvex</span>
      <span class="client-name">Brindle</span>
      <span class="client-name">Halden</span>
      <span class="client-badge" aria-label="Security badge"></span>
      <span class="client-badge square" aria-label="Privacy certificate"></span>
      <span class="client-badge" aria-label="Trust seal"></span>
    </div>
  </section>
</main>

<a class="carousel-arrow prev" href="#" aria-label="Previous">
  <svg width="24" height="36" viewBox="0 0 24 36"><path d="M20 2L4 18L20 34" fill="none" stroke="#2a78b8" stroke-width="6"/></svg>
</a>
<a class="carousel-arrow next" href="#" aria-label="Next">
  <svg width="24" height="36" viewBox="0 0 24 36"><path d="M4 2L20 18L4 34" fill="none" stroke="#2a78b8" stroke-width="6"/></svg>
</a>

<footer class="site-footer">
  <span>© All Rights Reserved The VELDA group Ltd 2013</span>
  <nav class="footer-nav">
    <a href="#">Home</a><span>|</span><a href="#">Services</a><span>|</span><a href="#">Clients</a><span>|</span><a href="#">Contact</a><span>|</span><a href="#">INSPIRE</a>
  </nav>
</footer>

</body>
</html>
```